Van and Ute Car wrap design

Looking for some funky ideas for a car wrap design for our product.
Us:
Solid Surface and engineered stone benchtop manufacturer for Kitchens, Bathrooms office fitouts and more

Suppliers: (could you maybe grab some of their logos to use)?
Brindlequarz
Veltarin
Zo-Pelt
Gorvamite
Quellarite
Baxwellite
Feldroy

Vehicles:
Korvanu E-vant 2012 (white)
Tavelonka Balsek 2018 (black)

Contact details:
sales@velmarobenchtops.com
www.velmarobenchtops.com
09 - 482 3915

Added some photos in and our logo. Would be good to see some options of what is possible?

```html
<!DOCTYPE html>
<html lang="en">
<head>
<meta charset="utf-8">
<title>Velmaro Benchtops – Ute Wrap Concepts</title>
<link rel="stylesheet" href="https://fonts.googleapis.com/css2?family=Archivo+Black&family=Montserrat:wght@400;500;700&display=swap">
<style>
  :root {
    --wrap-blue: #1d78c8;
    --wrap-black: #0d0f12;
    --glass: #3a3f46;
    --page: #ffffff;
    --label: #3b3b3b;
    --text-light: #ffffff;
  }
  html, body { margin: 0; padding: 0; overflow: hidden; background: var(--page); }
  .canvas { position: relative; width: 1200px; height: 1122px; overflow: hidden; }
  .sheet { position: absolute; inset: 0; width: 1200px; height: 1122px; }
  .concept-label { font-family: "Archivo Black", sans-serif; font-size: 34px; fill: var(--label); letter-spacing: 0.5px; }
  .brand-name { font-family: "Montserrat", sans-serif; font-weight: 400; fill: var(--wrap-blue); }
  .phone { font-family: "Montserrat", sans-serif; font-weight: 700; }
  .contact { font-family: "Montserrat", sans-serif; font-weight: 500; fill: var(--text-light); }
  .supplier { font-family: "Montserrat", sans-serif; font-weight: 500; fill: var(--text-light); font-size: 13px; }
</style>
</head>
<body>
<div class="canvas">
<svg class="sheet" viewBox="0 0 1200 1122" xmlns="http://www.w3.org/2000/svg">
  <defs>
    <path id="ute-body" d="M40,282 L395,268 L405,185 L420,178 L690,178 L850,265 L1110,295 L1175,335 L1185,430 L1160,465 L40,465 Z"/>
    <clipPath id="body-clip"><use href="#ute-body"/></clipPath>
    <linearGradient id="photo-tones" x1="0" y1="0" x2="1" y2="1">
      <stop offset="0" stop-color="#c9b79a"/>
      <stop offset="1" stop-color="#6e6458"/>
    </linearGradient>
    <linearGradient id="kitchen-tones" x1="0" y1="0" x2="1" y2="0">
      <stop offset="0" stop-color="#b98d5c"/>
      <stop offset="0.6" stop-color="#8c8a86"/>
      <stop offset="1" stop-color="#2a2b2e"/>
    </linearGradient>
  </defs>

  <!-- Concept 01 -->
  <text class="concept-label" x="88" y="110">Concept&#160;&#160;01</text>
  <g class="wrap concept-one">
    <g clip-path="url(#body-clip)">
      <rect class="panel-blue" x="0" y="150" width="1200" height="330" fill="var(--wrap-blue)"/>
      <polygon class="panel-black" points="30,255 420,250 870,342 870,392 800,462 440,475 30,300" fill="var(--wrap-black)"/>
      <polygon class="hood-black" points="980,300 1120,296 1180,340 1070,318" fill="var(--wrap-black)"/>
    </g>
    <polygon class="window" points="458,196 615,196 615,262 458,276" fill="var(--glass)"/>
    <polygon class="window" points="650,196 700,196 838,268 650,276" fill="var(--glass)"/>
    <circle cx="150" cy="318" r="30" fill="url(#photo-tones)" role="img" aria-label="Kitchen benchtop photo"/>
    <circle cx="215" cy="333" r="30" fill="url(#photo-tones)" role="img" aria-label="Cooktop in stone benchtop photo"/>
    <circle cx="284" cy="344" r="30" fill="url(#photo-tones)" role="img" aria-label="Bathroom vanity photo"/>
    <g class="suppliers">
      <text class="supplier" x="68" y="348" transform="rotate(8 68 348)">Feldroy</text>
      <text class="supplier" x="62" y="372" transform="rotate(8 62 372)">Zo-Pelt</text>
      <text class="supplier" x="140" y="372" transform="rotate(8 140 372)">Brindlequarz</text>
      <text class="supplier" x="135" y="396" font-size="15" transform="rotate(8 135 396)">Veltarin</text>
      <text class="supplier" x="82" y="404" transform="rotate(8 82 404)">Gorvamite</text>
    </g>
    <text class="contact" x="572" y="290" font-size="11" transform="rotate(12 572 290)">www.velmarobenchtops.com</text>
    <text class="brand-name" x="475" y="360" font-size="66" transform="rotate(12 475 360)">VELMARO</text>
    <text class="brand-name" x="462" y="394" font-size="25" letter-spacing="11" transform="rotate(14 462 394)">BENCHTOPS</text>
    <text class="phone" x="738" y="316" font-size="31" fill="var(--text-light)" transform="rotate(12 738 316)">09-482-3915</text>
    <text class="contact" x="734" y="334" font-size="15" transform="rotate(12 734 334)">sales@velmarobenchtops.com</text>
    <circle cx="330" cy="488" r="92" fill="var(--page)"/>
    <circle cx="1030" cy="488" r="92" fill="var(--page)"/>
  </g>

  <!-- Concept 02 -->
  <text class="concept-label" x="88" y="665">Concept&#160;&#160;02</text>
  <g class="wrap concept-two" transform="translate(0,555)">
    <g clip-path="url(#body-clip)">
      <rect class="panel-black" x="0" y="150" width="1200" height="330" fill="var(--wrap-black)"/>
      <polygon class="roof-blue" points="420,170 860,170 860,262 790,236 690,252 480,212" fill="var(--wrap-blue)"/>
      <polygon class="chevron-blue" points="560,248 685,318 810,248 785,248 685,300 585,248" fill="var(--wrap-blue)"/>
      <rect x="40" y="262" width="360" height="180" fill="url(#kitchen-tones)" role="img" aria-label="Kitchen with stone benchtop and stools"/>
      <rect class="band-blue" x="0" y="314" width="1200" height="52" fill="var(--wrap-blue)" opacity="0.92"/>
      <rect class="logo-plate" x="540" y="306" width="315" height="64" fill="var(--wrap-black)"/>
    </g>
    <polygon class="window" points="458,196 615,196 615,262 458,276" fill="var(--glass)"/>
    <polygon class="window" points="650,196 700,196 838,268 650,276" fill="var(--glass)"/>
    <text class="brand-name" x="697" y="362" font-size="56" text-anchor="middle">VELMARO</text>
    <text class="brand-name" x="700" y="389" font-size="20" letter-spacing="12" text-anchor="middle">BENCHTOPS</text>
    <text class="phone" x="866" y="303" font-size="23" fill="var(--wrap-blue)">09-482-3915</text>
    <text class="contact" x="490" y="418" font-size="11.5">sales@velmarobenchtops.com</text>
    <text class="contact" x="716" y="418" font-size="11.5">www.velmarobenchtops.com</text>
    <circle cx="330" cy="488" r="92" fill="var(--page)"/>
    <circle cx="1030" cy="488" r="92" fill="var(--page)"/>
  </g>
</svg>
</div>
</body>
</html>
```